Geschäftspapiere für Spezialist für Fliesen, Kaminöfen etc.
Zielgruppe
Wir sind ein Familienunternehmen in dritter Generation und Spezialist für Fliesen, Natursteine, Kaminöfen, Schwimmbäder und Whirlpools. Professionell, kreativ und voller Leidenschaft begleiten wir unsere Kunden bei der Umsetzung ihrer Vorhaben. Von der persönlichen Beratung bis hin zur Ausführung profitieren unsere Kunden von qualifiziertem Fachpersonal und 60 Jahren Erfahrung. Unsere Zielgruppe sind Familien/Paare ab 35 Jahren, die hochwertige Produkte für Ihr Zuhause suchen.
Aufgabenstellung
Wir benötigen neues Briefpapier, da wir ein neues Logo haben. Wir hätten gerne drei bis vier Bilder in der Kopfleiste. Des weiteren soll unser Portfolio aufgelistet sein (Fliesen, Natursteine, Kaminöfen, Schwimmbäder und Whirlpools). Das Logo soll in weiß gedruckt werden, der Hintergrund sollte daher dunkel sein (Farbton ähnlich DB703). Wir haben bereits selbst einen Entwurf gestaltet, in welche Richtung das Design gehen soll, sind jedoch offen für Ideen und Vorschläge.
Schriftart: z. B. Syncopate in Großbuchstaben

```html
<!DOCTYPE html>
<html lang="de">
<head>
<meta charset="utf-8">
<title>Briefbogen Marmor-Kessler</title>
<link href="https://fonts.googleapis.com/css2?family=Outfit:wght@300;400&display=swap" rel="stylesheet">
<style>
  :root {
    --backdrop: #d1c9c9;
    --paper: #ffffff;
    --band: #494544;
    --ink: #2f2c2c;
    --white: #ffffff;
    --rule: #555050;
    --mark: #9a9494;
    --bath-a: #e9e9ea; --bath-b: #b9b3ad;
    --fire-a: #c9b9a4; --fire-b: #5a4c44;
    --pool-a: #c9dcec; --pool-b: #7fae58;
  }
  * { margin: 0; padding: 0; box-sizing: border-box; }
  html, body { width: 960px; height: 1200px; overflow: hidden; background: var(--backdrop); }
  body { position: relative; font-family: "Outfit", sans-serif; font-weight: 300; color: var(--ink); }
  .sheet { position: absolute; left: 82px; top: 36px; width: 795px; height: 1124px; background: var(--paper); }
  .masthead { position: absolute; left: 0; top: 0; width: 795px; height: 156px; background: var(--band); }
  .masthead svg { position: absolute; left: 0; top: 0; }
  .brand {
    position: absolute; left: 561px; top: 42px; width: 186px; height: 54px;
    display: flex; align-items: center; justify-content: center;
    color: var(--white); font-size: 26px; font-weight: 400; letter-spacing: 0.22em;
  }
  .portfolio {
    position: absolute; left: 50px; right: 40px; top: 131px;
    display: flex; justify-content: space-between; list-style: none;
    color: var(--white); font-size: 14px; font-weight: 400; letter-spacing: 0.3em;
  }
  .sender-line { position: absolute; left: 96px; top: 189px; font-size: 11px; font-weight: 400; }
  .contact { position: absolute; left: 572px; top: 185px; font-size: 13.5px; line-height: 16px; }
  .contact p + p { margin-top: 16px; }
  .fold-mark { position: absolute; left: 0; width: 13px; height: 1px; background: var(--mark); }
  .fold-mark.punch { background: var(--ink); }
  .footer-rule { position: absolute; left: 0; top: 1045px; width: 795px; height: 1px; background: var(--rule); }
  .footer-col { position: absolute; top: 1054px; font-size: 13.5px; line-height: 16px; }
  .bank { left: 302px; }
  .tax { left: 572px; }
  .blz-value { margin-left: 20px; word-spacing: 4px; }
</style>
</head>
<body>
  <div class="sheet">
    <header class="masthead">
      <svg width="795" height="160" viewBox="0 0 795 160">
        <defs>
          <linearGradient id="bathTone" x1="0" y1="0" x2="1" y2="1">
            <stop offset="0" stop-color="var(--bath-a)"/><stop offset="1" stop-color="var(--bath-b)"/>
          </linearGradient>
          <linearGradient id="fireTone" x1="0" y1="0" x2="1" y2="1">
            <stop offset="0" stop-color="var(--fire-a)"/><stop offset="1" stop-color="var(--fire-b)"/>
          </linearGradient>
          <linearGradient id="poolTone" x1="0" y1="0" x2="0" y2="1">
            <stop offset="0" stop-color="var(--pool-a)"/><stop offset="1" stop-color="var(--pool-b)"/>
          </linearGradient>
        </defs>
        <polygon role="img" aria-label="Foto: helles Badezimmer mit Marmorfliesen und freistehender Wanne" points="0,0 190,0 149,111 0,111" fill="url(#bathTone)"/>
        <polygon role="img" aria-label="Foto: Wohnraum mit Kaminofen vor Natursteinwand" points="194,21 416,21 387,123 171,123" fill="url(#fireTone)"/>
        <polygon role="img" aria-label="Foto: moderne Villa mit Schwimmbecken im Garten" points="416,0 613,0 575,111 390,111" fill="url(#poolTone)"/>
      </svg>
      <div class="brand">KESSLER</div>
      <ul class="portfolio">
        <li>FLIESEN</li><li>NATURSTEINE</li><li>KAMINÖFEN</li><li>SCHWIMMBÄDER</li><li>WHIRLPOOLS</li>
      </ul>
    </header>

    <p class="sender-line">Marmor-Kessler GmbH · Lindenweg 7 · 76829 Talheim</p>

    <address class="contact" style="font-style:normal">
      <p>Marmor-Kessler GmbH<br>Lindenweg 7<br>76829 Talheim</p>
      <p>Tel.: +49 6341 482170<br>info@marmor-kessler.de</p>
    </address>

    <span class="fold-mark" style="top:396px"></span>
    <span class="fold-mark punch" style="top:559px"></span>
    <span class="fold-mark" style="top:793px"></span>

    <div class="footer-rule"></div>
    <div class="footer-col bank">
      Kontoverbindung<br>
      IBAN: DE00 1111 2222 3333 4444 55<br>
      BLZ:<span class="blz-value">000 000 000</span>
    </div>
    <div class="footer-col tax">
      Gerichtsstand xxxxxxxxx<br>
      Steuer-Nr. 111/222/00000<br>
      Finanzamt XYZXYZXYZ
    </div>
  </div>
</body>
</html>
```